Business Card Design Project

We need a redesign of our business card.
We are a Consulting Property Developer called The Kestrel Group
Updates

Thank you all for submissions. Just waiting on managment to decide.

Thank you,

Dorinda

Industry/Entity Type

Business

Requirements
Must have
• we like having the KG a focus in the back ground or on the side
Kestrel is our company colour

the wording - property development
and - premium accommodation

our website www.kestrelgroup-example.com.au

persons name
title

p: 1300 482917 f: 1300 482915 m: 0417593824
PO Box 5817, Brindlevale Qld 4178
e: admin@kestrelgroup-example.com.au

```html
<!DOCTYPE html>
<html lang="en">
<head>
<meta charset="utf-8">
<title>The Kestrel Group – Business Card</title>
<link rel="stylesheet" href="https://fonts.googleapis.com/css2?family=PT+Sans+Narrow:wght@400;700&family=PT+Sans:wght@400;700&display=swap">
<style>
  :root {
    --kestrel: #8e1a35;
    --kestrel-soft: #c9606a;
    --blush: #e6a9b4;
    --ink: #333333;
    --frame: #7a7a7a;
    --paper: #ffffff;
  }
  * { margin: 0; padding: 0; box-sizing: border-box; }
  html, body {
    width: 1200px;
    height: 849px;
    overflow: hidden;
    background: var(--paper);
  }
  .stage {
    position: relative;
    width: 1200px;
    height: 849px;
  }
  .business-card {
    position: absolute;
    left: 402px;
    top: 306px;
    width: 367px;
    height: 204px;
    background: var(--paper);
    border: 1.5px solid var(--frame);
    overflow: hidden;
    font-family: "PT Sans Narrow", "Arial Narrow", sans-serif;
  }
  .halo {
    position: absolute;
    left: -50px;
    top: -42px;
    width: 282px;
    height: 282px;
    border-radius: 50%;
    background: radial-gradient(circle at 50% 50%,
      #ffffff 0%, #ffffff 58%, #fbeef1 76%, #f1cdd5 90%, var(--blush) 100%);
  }
  .brand-name {
    position: absolute;
    left: 14px;
    top: 90px;
    width: 180px;
    text-align: center;
    font-family: "PT Sans Narrow", "Arial Narrow", sans-serif;
    font-weight: 700;
    font-size: 22px;
    color: var(--kestrel);
    letter-spacing: 0.2px;
  }
  .services {
    position: absolute;
    left: 276px;
    top: 51px;
    font-weight: 700;
    font-size: 9px;
    line-height: 11px;
    color: var(--kestrel);
    list-style: none;
  }
  .name-panel {
    position: absolute;
    left: 275px;
    top: 74px;
    width: 92px;
    height: 50px;
    background: var(--kestrel-soft);
    padding: 15px 0 0 7px;
    color: #ffffff;
    font-weight: 700;
    font-size: 7.5px;
    line-height: 10px;
  }
  .contact {
    position: absolute;
    left: 200px;
    top: 173px;
    width: 172px;
    text-align: center;
    font-family: "PT Sans", Arial, sans-serif;
    font-size: 6.4px;
    line-height: 8.2px;
    color: var(--ink);
    font-style: normal;
  }
  .contact .label {
    color: var(--kestrel);
    font-weight: 700;
  }
</style>
</head>
<body>
  <main class="stage">
    <section class="business-card" aria-label="The Kestrel Group business card">
      <div class="halo" aria-hidden="true"></div>
      <p class="brand-name">The Kestrel Group</p>

      <ul class="services">
        <li>property development</li>
        <li>premium accommodation</li>
      </ul>

      <div class="name-panel">
        <p class="person-name">persons name</p>
        <p class="person-title">title</p>
      </div>

      <address class="contact">
        <p><span class="label">p:</span> 1300 482917&nbsp; <span class="label">f:</span> 1300 482915&nbsp; <span class="label">m:</span> 0417593824</p>
        <p>PO Box 5817, Brindlevale Qld 4178</p>
        <p><span class="label">e:</span> admin@kestrelgroup-example.com.au</p>
      </address>
    </section>
  </main>
</body>
</html>
```